existing Business Card Re design

We are wanting to re design our cards to reflect our new logo , i have attache the current business cards and new logo
i will need a business card that reflects the following information on each card.

card 1:
Gordon Thibeaux, President
555-182-4407
info@qlmcoatingpro.example

card 2:
Lionel Ostrander, Outside Sales
Office: 555-182-4407
Cell: 555-631-2958
Sales@qlmcoatingpro.example

Card 3
Tomas Varley, Branch Manager
Office: 555-182-4407
Cell: 555-274-8163
Tomas@qlmcoatingpro.example

Card 4
I will need a Generic card with no name on it just business
555-182-4407
info@qlmcoatingpro.example

Target Market(s)

Homeowners and Contractors

Contact Information for Business Card

We are wanting to re design our cards to reflect our new logo , i have attache the current business cards and new logo. same info on current card

card 1:
Gordon Thibeaux, President
555-182-4407
info@qlmcoatingpro.example

card 2:
Office: 555-182-4407
Cell: 555-631-2958
Sales@qlmcoatingpro.example

Card 3
Office: 555-182-4407
Cell: 555-274-8163
Tomas@qlmcoatingpro.example

Card 4
555-182-4407
info@qlmcoatingpro.example

Requirements
Must have
• same info as current cards with a added business
"sanitizing"

```html
<!DOCTYPE html>
<html lang="en">
<head>
<meta charset="utf-8">
<title>QLM Coating Pro – Business Card</title>
<link href="https://fonts.googleapis.com/css2?family=Montserrat:wght@400;500;700;800&display=swap" rel="stylesheet">
<style>
  :root {
    --page-bg: #2a2a2a;
    --blue-bright: #1f9ad8;
    --blue-mid: #1a4f96;
    --blue-deep: #2b3d86;
    --ink-dark: #0b0d14;
    --white: #ffffff;
    --divider: #0c0c10;
  }
  * { box-sizing: border-box; margin: 0; padding: 0; }
  html, body {
    width: 1200px; height: 988px; overflow: hidden;
    background: var(--page-bg);
    font-family: "Montserrat", sans-serif;
  }
  .card {
    position: absolute;
    width: 560px; height: 320px;
    border-radius: 22px;
    overflow: hidden;
    box-shadow: 0 14px 30px rgba(0,0,0,.55);
  }
  /* front */
  .card-front {
    left: 70px; top: 110px;
    background: linear-gradient(160deg, var(--blue-bright) 0%, var(--blue-mid) 45%, var(--ink-dark) 85%);
    color: var(--white);
    display: flex; flex-direction: column; align-items: center; justify-content: center;
  }
  .brand {
    display: flex; align-items: center; gap: 14px;
  }
  .brand-mark {
    width: 34px; height: 34px; background: currentColor;
  }
  .brand-name {
    font-weight: 800; font-size: 40px; letter-spacing: -0.5px; line-height: 1;
  }
  .social {
    margin-top: 44px;
    display: flex; align-items: center; gap: 10px;
    font-size: 15px; font-weight: 400; letter-spacing: .3px;
  }
  .social-dot {
    width: 20px; height: 20px; border-radius: 50%; background: var(--white);
  }
  /* back */
  .card-back {
    left: 570px; top: 560px;
    display: flex;
  }
  .back-logo {
    width: 49%;
    background: var(--white);
    color: var(--blue-mid);
    display: flex; align-items: center; justify-content: center;
  }
  .back-logo .brand-name { font-size: 25px; }
  .back-logo .brand-mark { width: 24px; height: 24px; }
  .back-logo .brand { gap: 10px; }
  .back-divider { width: 8px; background: var(--divider); }
  .back-info {
    flex: 1;
    background: linear-gradient(200deg, var(--blue-deep) 0%, #2a6cb0 45%, var(--blue-bright) 100%);
    color: var(--white);
    padding: 44px 30px 0 30px;
  }
  .person-name { font-size: 22px; font-weight: 700; letter-spacing: .3px; }
  .person-title { font-size: 12px; font-weight: 400; margin-top: 2px; }
  .rule { height: 1px; background: rgba(255,255,255,.85); margin: 12px 0; }
  .address { font-size: 12px; line-height: 1.35; }
  .contact-list { list-style: none; font-size: 12.5px; line-height: 1.55; }
  .contact-list li { display: flex; align-items: center; gap: 8px; }
  .contact-list svg { width: 12px; height: 12px; flex: none; fill: var(--white); }
</style>
</head>
<body>

<section class="card card-front" aria-label="Card front">
  <div class="brand">
    <span class="brand-mark"></span>
    <span class="brand-name">QLM Coating Pro</span>
  </div>
  <div class="social">
    <span class="social-dot"></span>
    <span>qlmcoatingpro</span>
  </div>
</section>

<section class="card card-back" aria-label="Card back">
  <div class="back-logo">
    <div class="brand">
      <span class="brand-mark"></span>
      <span class="brand-name">QLM Coating Pro</span>
    </div>
  </div>
  <div class="back-divider"></div>
  <div class="back-info">
    <h1 class="person-name">Gordon Thibeaux</h1>
    <p class="person-title">President</p>
    <div class="rule"></div>
    <p class="address">4820 Larkspur Ave.<br>Suite 5 Fairview, TX 75000</p>
    <div class="rule"></div>
    <ul class="contact-list">
      <li>
        <svg viewBox="0 0 24 24" aria-hidden="true"><path d="M6.6 10.8a15.1 15.1 0 0 0 6.6 6.6l2.2-2.2a1 1 0 0 1 1-.25 11.4 11.4 0 0 0 3.6.57 1 1 0 0 1 1 1V20a1 1 0 0 1-1 1A17 17 0 0 1 3 4a1 1 0 0 1 1-1h3.5a1 1 0 0 1 1 1c0 1.25.2 2.45.57 3.57a1 1 0 0 1-.25 1z"/></svg>
        555-182-4407
      </li>
      <li>
        <svg viewBox="0 0 24 24" aria-hidden="true"><path d="M2 5h20v14H2zm2 2v.4l8 5.2 8-5.2V7zm0 2.8V17h16V9.8l-8 5.2z"/></svg>
        info@qlmcoatingpro.example
      </li>
      <li>
        <svg viewBox="0 0 24 24" aria-hidden="true"><path d="M12 2a10 10 0 1 0 0 20 10 10 0 0 0 0-20zm6.9 6h-3a15.6 15.6 0 0 0-1.4-4A8 8 0 0 1 18.9 8zM12 4c.8 1.2 1.5 2.5 1.9 4h-3.8c.4-1.5 1.1-2.8 1.9-4zM4.3 14a8 8 0 0 1 0-4h3.4a16 16 0 0 0 0 4zm.8 2h3a15.6 15.6 0 0 0 1.4 4A8 8 0 0 1 5.1 16zM8 8H5.1a8 8 0 0 1 4.4-4A15.6 15.6 0 0 0 8 8zm4 12c-.8-1.2-1.5-2.5-1.9-4h3.8c-.4 1.5-1.1 2.8-1.9 4zm2.3-6H9.7a14.7 14.7 0 0 1 0-4h4.6a14.7 14.7 0 0 1 0 4zm.2 6a15.6 15.6 0 0 0 1.4-4h3a8 8 0 0 1-4.4 4zm1.8-6a16 16 0 0 0 0-4h3.4a8 8 0 0 1 0 4z"/></svg>
        qlmcoatingpro.example
      </li>
    </ul>
  </div>
</section>

</body>
</html>
```